Harlow Benefit Advisory - Statonery Design

I just completed a redesign of my business card. Please do not design a logo or business card. See my current stationery design attached.

Target Market(s)

VP of Human Resources and Finance - Companies with 100 employees to 10,000

Industry/Entity Type

Business Consultant

Requirements
Must have
• Use the letterhead instructions for the color and fonts.

```html
<!DOCTYPE html>
<html lang="en">
<head>
<meta charset="utf-8">
<title>Harlow Benefit Advisory – Stationery</title>
<link href="https://fonts.googleapis.com/css2?family=Open+Sans:wght@400;600&display=swap" rel="stylesheet">
<style>
  :root {
    --plum: #6b1d4a;
    --ink: #2b2b2b;
    --grey: #6e6e6e;
    --paper: #fbfbfb;
    --backdrop: #2f2f2f;
    --signature-tone: #d9c3cf;
  }
  * { box-sizing: border-box; margin: 0; padding: 0; }
  html, body { width: 1200px; height: 1200px; overflow: hidden; }
  body {
    background: var(--backdrop);
    font-family: "Open Sans", Arial, sans-serif;
    color: var(--ink);
    position: relative;
  }

  /* Company name */
  .company-name {
    font-family: "Open Sans", Arial, sans-serif;
    font-weight: 400;
    color: var(--ink);
    font-size: 18px;
    white-space: nowrap;
  }

  /* Letterhead */
  .letterhead {
    position: absolute; left: 60px; top: 212px;
    width: 600px; height: 776px;
    background: var(--paper);
  }
  .letterhead .company-name { position: absolute; left: 50px; top: 62px; }
  .contact-list {
    position: absolute; right: 48px; top: 44px;
    list-style: none; font-size: 10.5px; line-height: 16px; color: var(--ink);
  }
  .contact-list li { display: flex; align-items: center; gap: 6px; }
  .contact-list svg { width: 10px; height: 10px; fill: var(--plum); flex: none; }

  .recipient {
    position: absolute; left: 50px; top: 180px;
    font-size: 10.5px; line-height: 19px; color: var(--ink);
  }
  .letter-body {
    position: absolute; left: 50px; right: 50px; top: 262px;
    font-size: 10.5px; line-height: 18px; color: var(--ink);
  }
  .letter-body p + p { margin-top: 16px; }

  .closing { position: absolute; left: 50px; top: 560px; }
  .closing-line { font-size: 13px; color: var(--grey); }
  .signature {
    width: 190px; height: 48px; margin: 8px 0 4px;
    background: linear-gradient(90deg, var(--signature-tone), #f0e4ea);
    border-radius: 4px;
  }
  .signer-title { font-size: 13px; font-weight: 600; color: var(--ink); }

  .letterhead-address {
    position: absolute; right: 50px; bottom: 34px;
    font-size: 12.5px; color: var(--ink);
  }
  .letterhead-band {
    position: absolute; left: 0; right: 0; bottom: 0; height: 14px;
    background: var(--plum);
  }

  /* Envelope */
  .envelope {
    position: absolute; left: 690px; top: 500px;
    width: 460px; height: 200px;
    background: var(--paper);
  }
  .envelope .company-name { position: absolute; left: 28px; top: 28px; font-size: 14px; }
  .envelope-return {
    position: absolute; left: 28px; bottom: 30px;
    font-size: 9.5px; line-height: 14px;
  }
  .envelope-web { font-weight: 600; color: var(--ink); }
  .envelope-web span { color: var(--plum); }
  .envelope-band {
    position: absolute; left: 0; right: 0; bottom: 0; height: 12px;
    background: var(--plum);
  }
</style>
</head>
<body>

<section class="letterhead">
  <p class="company-name">Harlow Benefit Advisory</p>

  <ul class="contact-list">
    <li><svg viewBox="0 0 10 10"><path d="M1 3.5C1 2 2 1 5 1s4 1 4 2.5H7L6.5 2.5h-3L3 3.5zM2 5l1.5-1h3L8 5v4H2z"/></svg>555.210.4471</li>
    <li><svg viewBox="0 0 10 10"><rect x="2.5" y="0.5" width="5" height="9" rx="1"/><rect x="3.3" y="1.5" width="3.4" height="5.5" fill="#fbfbfb"/></svg>555.318.2096</li>
    <li><svg viewBox="0 0 10 10"><rect x="1" y="4" width="8" height="5" rx="0.8"/><rect x="3" y="1" width="4" height="3.5" fill="none" stroke="#6b1d4a" stroke-width="0.9"/></svg>555.210.4472</li>
    <li><svg viewBox="0 0 10 10"><circle cx="5" cy="5" r="4.3" fill="none" stroke="#6b1d4a" stroke-width="1"/><path d="M0.7 5h8.6M5 0.7c-2.2 2.4-2.2 6.2 0 8.6M5 0.7c2.2 2.4 2.2 6.2 0 8.6" fill="none" stroke="#6b1d4a" stroke-width="0.8"/></svg>www.harlowbenefit.com</li>
  </ul>

  <div class="recipient">
    <p>To</p>
    <p>The,</p>
    <p>Director</p>
  </div>

  <div class="letter-body">
    <p>Lorem ipsum dolor sit amet, consectetur adipiscing elit. Sed at ante. Mauris eleifend, quam a vulputate dictum, massa quam dignissim nunc, vulputate orci purus ut lorem. In fringilla mi in ligula. Pellentesque aliquam, nibh sed congue porta. Sed quamodio, tempus ac, aliquam molestie varius ac, tellus. Vestibulum rhoncus mi in interdum. Pellentesque lorem.</p>
    <p>Integer dictum lorem et erat viverra. Pellentesque augue justo, sagittis et, lacinia at, venenatis non, arcu. Nunc fermentum risus. Etiam tristique nisl a nulla. Ut a orci. Curabitur dolor nunc, egestas malesuada nec, magna. Nulla facilisi. Nunc volutpat. Vestibulum ante ipsum primis in ultrices posuere cubilia Curae; Ut sit amet orci vel mauris blandit fermentum. Donec dignissim viverra velit. Curabitur in odio.</p>
    <p>Aliquam erat volutpat consequat, tellus eu volutpat varius, justo orci elementum dolor, sed imperdiet nulla sit amet ipsum ante, malesuada quis, tempus ac, placerat sit amet, elit.</p>
  </div>

  <div class="closing">
    <p class="closing-line">Thanking you,</p>
    <div class="signature" role="img" aria-label="Handwritten signature of Daniel Hartwell"></div>
    <p class="signer-title">President</p>
  </div>

  <p class="letterhead-address">418 Harbor Street NW, Suite 200, Lakeview, MI 49320</p>
  <div class="letterhead-band"></div>
</section>

<section class="envelope">
  <p class="company-name">Harlow Benefit Advisory</p>
  <div class="envelope-return">
    <p class="envelope-web">www.<span>harlowbenefit</span>.com</p>
    <p>418 Harbor Street NW, Suite 200, Lakeview, MI 49320</p>
  </div>
  <div class="envelope-band"></div>
</section>

</body>
</html>
```